New Business Card Design Project

We are looking for a talented individual to create a truly awesome/unique business card design for us. We are looking for a someone to design something that will really stand out from the crowd - we don't mind what ideas you come up with (ie embossed/flat/matte/shine etc etc) just wow us with your creativity.
Updates

Target Market(s)

Video Games Industry Professionals (all levels of seniority from QA Testers through to CEOs)

Contact Information for Business Card

Company logo (see upload)
Company name: Northbay Play Careers Ltd
Employee Name: Darren Elsby
Job title: CEO
Website: www.nbpc2go.example
Office +44 1632 960418
Mobile: +44 7700 900276
Email: darren@nbpc2go.example

Colors

Designer to choose colors to be used in the design.

Requirements
Must have
• The business card design MUST contain all the information listed in the BUSINESS CARD DETAILS box.
• You will see the colours that are relevant to us (ie company logo) in the uploaded imagery - however you do not have to use all these colours when designing the business card itself
• MUST BE DOUBLE SIDED

```html
<!DOCTYPE html>
<html lang="en">
<head>
<meta charset="utf-8">
<title>Northbay Play Careers – Business Card</title>
<link rel="stylesheet" href="https://fonts.googleapis.com/css2?family=Exo+2:wght@600;700&family=Roboto:wght@400&display=swap">
<style>
  :root {
    --stage: #2b2b2d;
    --charcoal: #3b3b3e;
    --charcoal-deep: #2f2f32;
    --navy: #1f3a8f;
    --navy-ink: #1c2f6e;
    --orange: #f28a1e;
    --paper: #ffffff;
    --ink: #2e2e33;
    --muted: #6b6b72;
  }
  * { box-sizing: border-box; margin: 0; padding: 0; }
  html, body { width: 1200px; height: 874px; overflow: hidden; }
  body {
    background: var(--stage);
    position: relative;
    font-family: "Roboto", sans-serif;
  }
  .card {
    position: absolute;
    left: 290px;
    width: 620px;
    height: 354px;
    border-radius: 4px;
    overflow: hidden;
    box-shadow: 0 10px 28px rgba(0,0,0,.45);
  }
  /* Back side */
  .card-back {
    top: 43px;
    background: radial-gradient(circle at 50% 45%, var(--charcoal) 0%, var(--charcoal-deep) 100%);
    display: flex;
    align-items: center;
    justify-content: center;
  }
  .back-mark {
    display: flex;
    align-items: center;
    gap: 16px;
  }
  .back-mark .dot {
    width: 64px; height: 64px;
    border-radius: 50%;
    background: var(--navy);
  }
  .back-mark .name {
    font-family: "Exo 2", sans-serif;
    font-weight: 700;
    font-size: 30px;
    color: #d9dbe2;
    letter-spacing: .5px;
  }
  /* Front side */
  .card-front {
    top: 437px;
    background: var(--paper);
  }
  .wave { position: absolute; inset: 0; width: 620px; height: 354px; }
  .holder {
    position: absolute;
    right: 34px;
    top: 66px;
    text-align: right;
    color: var(--paper);
  }
  .holder-name {
    font-family: "Exo 2", sans-serif;
    font-weight: 700;
    font-size: 27px;
    letter-spacing: .5px;
  }
  .holder-title {
    font-size: 15px;
    margin-top: 2px;
  }
  .brand {
    position: absolute;
    left: 40px;
    top: 150px;
    display: flex;
    align-items: center;
    gap: 10px;
  }
  .brand .dot {
    width: 38px; height: 38px;
    border-radius: 50%;
    background: var(--navy-ink);
  }
  .brand .name {
    font-family: "Exo 2", sans-serif;
    font-weight: 700;
    font-size: 22px;
    line-height: 1.05;
    color: var(--navy-ink);
    width: 170px;
  }
  .contacts {
    position: absolute;
    left: 40px;
    top: 222px;
    list-style: none;
    font-size: 15px;
    color: var(--ink);
  }
  .contacts li {
    display: flex;
    align-items: center;
    gap: 9px;
    height: 21px;
  }
  .contacts svg { width: 13px; height: 13px; fill: var(--navy-ink); flex: none; }
  .legal {
    position: absolute;
    right: 30px;
    bottom: 22px;
    font-size: 15px;
    color: var(--muted);
  }
</style>
</head>
<body>

<section class="card card-back" aria-label="Card back">
  <div class="back-mark">
    <span class="dot"></span>
    <span class="name">Northbay Play Careers</span>
  </div>
</section>

<section class="card card-front" aria-label="Card front">
  <svg class="wave" viewBox="0 0 620 354" aria-hidden="true">
    <path d="M0 0 H620 V182 C520 170 430 160 360 130 C270 90 170 30 0 40 Z" fill="var(--orange)"/>
    <path d="M0 0 H620 V168 C520 156 430 146 360 116 C270 76 170 18 0 26 Z" fill="var(--navy)"/>
  </svg>

  <div class="holder">
    <div class="holder-name">Darren Elsby</div>
    <div class="holder-title">CEO</div>
  </div>

  <div class="brand">
    <span class="dot"></span>
    <span class="name">Northbay Play Careers</span>
  </div>

  <ul class="contacts">
    <li>
      <svg viewBox="0 0 24 24"><path d="M6.6 10.8a15 15 0 0 0 6.6 6.6l2.2-2.2c.3-.3.7-.4 1-.2 1.1.4 2.3.6 3.6.6.6 0 1 .4 1 1V20c0 .6-.4 1-1 1A17 17 0 0 1 3 4c0-.6.4-1 1-1h3.5c.6 0 1 .4 1 1 0 1.3.2 2.5.6 3.6.1.3 0 .7-.2 1z"/></svg>
      +44 1632 960418
    </li>
    <li>
      <svg viewBox="0 0 24 24"><path d="M7 1h10a2 2 0 0 1 2 2v18a2 2 0 0 1-2 2H7a2 2 0 0 1-2-2V3a2 2 0 0 1 2-2zm0 3v14h10V4z"/></svg>
      +44 7700 900276
    </li>
    <li>
      <svg viewBox="0 0 24 24"><path d="M2 5h20v14H2zm2 2v.5l8 5 8-5V7z"/></svg>
      darren@nbpc2go.example
    </li>
    <li>
      <svg viewBox="0 0 24 24"><circle cx="12" cy="12" r="10"/></svg>
      www.nbpc2go.example
    </li>
  </ul>

  <div class="legal">Northbay Play Careers Ltd</div>
</section>

</body>
</html>
```